Hip Music Management Co. BIz Card

I have a logo (attached) the back side of the card should the full logo on the entire card- that's it. The front side of the card should show the logo somewhere, keeping with the 4 different shades of blue. The front side of the card can be a white background with logo and colored typeface for all info. Pretty simple.

Target Market(s)

I manage and produce a whole bunch of major label and indie artists.

Industry/Entity Type

Management

Contact Information for Business Card

Velmora Sound House (logo)
Dale Fornwick
President
www.velmorasoundhouse.com
dale@velmorasoundhouse.com
+1 310.555.7182
418 Willow Bend Lane
Ashgrove Falls, NY 10599

Requirements
Must have
• Entire logo on back side. White background on front- unless you provide something more interesting.
Nice to have
• On the front of the card if you choose a white backgound, if possible take my logo without the blue background (over white) that would be cool.

```html
<!DOCTYPE html>
<html lang="en">
<head>
<meta charset="utf-8">
<title>Velmora Sound House – Business Card</title>
<link rel="stylesheet" href="https://fonts.googleapis.com/css2?family=Exo+2:wght@500;600&display=swap">
<style>
  :root {
    --backdrop: #d9d9d9;
    --card-black: #0c0c0d;
    --card-grey: #26272a;
    --sky: #5bb6f0;
    --teal: #1fc4c8;
    --band-blue: #4a4f9a;
    --badge-blue: #3d4a8e;
    --badge-edge: #6e86d6;
    --gold: #a79e72;
    --gold-dark: #7b7350;
    --brick: #8a2a22;
  }
  * { margin: 0; padding: 0; box-sizing: border-box; }
  html, body { width: 1200px; height: 900px; overflow: hidden; }
  body {
    background: var(--backdrop);
    font-family: "Exo 2", sans-serif;
    position: relative;
  }
  .card {
    position: absolute;
    left: 250px;
    width: 700px;
    height: 400px;
    border-radius: 14px;
    overflow: hidden;
    background: radial-gradient(ellipse at 60% 35%, var(--card-grey) 0%, var(--card-black) 70%);
    box-shadow: 0 10px 24px rgba(0,0,0,.35);
  }
  .card--front { top: 30px; }
  .card--back { top: 470px; }

  /* front */
  .brand-badge {
    position: absolute;
    top: 30px; right: 40px;
    width: 255px; height: 70px;
    border-radius: 8px;
    background: linear-gradient(180deg, #55619f 0%, var(--badge-blue) 100%);
    border: 1px solid var(--badge-edge);
    display: flex; align-items: center; justify-content: center;
  }
  .brand-name {
    font-weight: 600;
    font-size: 21px;
    color: var(--teal);
    letter-spacing: .5px;
  }
  .holder { position: absolute; left: 34px; top: 150px; }
  .holder__name { font-weight: 600; font-size: 40px; color: var(--sky); letter-spacing: 1px; line-height: 1; }
  .holder__role { font-weight: 600; font-size: 25px; color: var(--teal); letter-spacing: 2px; margin-top: 6px; }
  .divider {
    position: absolute; left: 0; right: 0; top: 238px; height: 8px;
    background: linear-gradient(90deg, var(--band-blue), #5a60b0);
  }
  .contacts { position: absolute; left: 36px; top: 275px; list-style: none; }
  .contacts li {
    display: flex; align-items: center; gap: 12px;
    font-size: 21px; font-weight: 500; color: var(--sky);
    height: 34px;
  }
  .contacts svg { width: 22px; height: 22px; flex: none; }
  .address {
    position: absolute; right: 40px; top: 268px;
    font-size: 20px; font-weight: 500; color: var(--sky);
    line-height: 1.3; text-align: left;
  }

  /* back */
  .feature-band {
    position: absolute; left: 40px; right: 40px; top: 100px; height: 200px;
    border-radius: 4px;
    background: radial-gradient(ellipse at 50% 50%, var(--gold) 0%, var(--gold-dark) 100%);
    display: flex; align-items: center; justify-content: center;
  }
  .feature-band .brand-name { color: var(--brick); font-size: 44px; }
</style>
</head>
<body>
  <section class="card card--front" aria-label="Card front">
    <div class="brand-badge"><span class="brand-name">Velmora Sound House</span></div>
    <div class="holder">
      <p class="holder__name">Dale Fornwick</p>
      <p class="holder__role">PRESIDENT</p>
    </div>
    <div class="divider"></div>
    <ul class="contacts">
      <li>
        <svg viewBox="0 0 22 22" fill="none" stroke="#5bb6f0" stroke-width="1.5"><circle cx="11" cy="11" r="10"/><path d="M7.5 6.5c0 4.5 3.5 8.5 8 9l1-2-2-1.2-1 1c-1.5-.7-3-2.2-3.7-3.7l1-1-1.2-2z"/></svg>
        +1 310.555.7182
      </li>
      <li>
        <svg viewBox="0 0 22 22" fill="none" stroke="#5bb6f0" stroke-width="1.5"><circle cx="11" cy="11" r="10"/><rect x="6" y="7.5" width="10" height="7"/><path d="M6 7.5l5 4 5-4"/></svg>
        dale@velmorasoundhouse.com
      </li>
      <li>
        <svg viewBox="0 0 22 22" fill="none" stroke="#5bb6f0" stroke-width="1.5"><circle cx="11" cy="11" r="10"/><ellipse cx="11" cy="11" rx="4" ry="10"/><path d="M1 11h20M3 6h16M3 16h16"/></svg>
        www.velmorasoundhouse.com
      </li>
    </ul>
    <p class="address">418 Willow Bend Lane<br>Ashgrove Falls,<br>NY 10599</p>
  </section>

  <section class="card card--back" aria-label="Card back">
    <div class="feature-band"><span class="brand-name">Velmora Sound House</span></div>
  </section>
</body>
</html>
```